Dova Lenthe Christmas Card 2025

I need a Christmas card design for Dova Lenthe (www.dovalenthe.example). My client loves everything Mara Quillon. I’ve attached this year’s inspirations, including the live wreath she is gifting and the brand guidelines. She prefers the softer colors shown in the inspiration materials. The greeting should read Merry Christmas (not Happy Holidays). The final design should feel elegant, festive, and aligned with the Dova Lenthe brand.”

```html
<!DOCTYPE html>
<html lang="en">
<head>
<meta charset="utf-8">
<title>Dova Lenthe — Merry Christmas Card</title>
<link rel="stylesheet" href="https://fonts.googleapis.com/css2?family=DM+Serif+Display&display=swap">
<style>
  :root {
    --backdrop: #e9e4dc;
    --card-cream: #fdf4e6;
    --greeting-orange: #f0852a;
    --glow-white: rgba(255, 255, 255, 0.95);
    --wreath-lavender: #6f6488;
    --wreath-olive: #8f9260;
    --wreath-leaf: #5f8a45;
    --wreath-pine: #3f6d2c;
    --wreath-sage: #9aa57a;
  }
  * { margin: 0; padding: 0; box-sizing: border-box; }
  html, body {
    width: 1200px;
    height: 1000px;
    overflow: hidden;
    background: var(--backdrop);
  }
  .card {
    position: absolute;
    left: 170px;
    top: 70px;
    width: 860px;
    height: 860px;
    background: var(--card-cream);
    box-shadow: 0 10px 30px rgba(0, 0, 0, 0.12);
  }
  .wreath {
    position: absolute;
    left: 50px;
    top: 32px;
    width: 780px;
    height: 780px;
  }
  .greeting {
    position: absolute;
    left: 0;
    right: 0;
    top: 296px;
    text-align: center;
    font-family: "DM Serif Display", serif;
    font-size: 118px;
    line-height: 0.92;
    color: var(--greeting-orange);
    text-shadow: 0 0 18px var(--glow-white), 0 0 8px var(--glow-white);
    padding-left: 20px;
  }
  .brand-mark {
    position: absolute;
    right: 42px;
    bottom: 40px;
    display: flex;
    align-items: center;
    gap: 10px;
    font-family: "DM Serif Display", serif;
    font-size: 30px;
    color: var(--greeting-orange);
  }
  .brand-dot {
    width: 16px;
    height: 16px;
    border-radius: 50%;
    background: var(--greeting-orange);
  }
</style>
</head>
<body>
  <main class="card">
    <svg class="wreath" viewBox="0 0 780 780" role="img" aria-label="Illustrated herb wreath of lavender, olive, bay leaves, sage and pine with orange berries and an orange slice">
      <defs>
        <linearGradient id="wreath-tones" x1="0" y1="0" x2="1" y2="1">
          <stop offset="0" stop-color="var(--wreath-lavender)"/>
          <stop offset="0.35" stop-color="var(--wreath-olive)"/>
          <stop offset="0.55" stop-color="var(--wreath-leaf)"/>
          <stop offset="0.8" stop-color="var(--wreath-pine)"/>
          <stop offset="1" stop-color="var(--wreath-sage)"/>
        </linearGradient>
      </defs>
      <circle cx="390" cy="390" r="285" fill="none" stroke="url(#wreath-tones)" stroke-width="210"/>
    </svg>

    <h1 class="greeting">Merry<br>Christmas</h1>

    <div class="brand-mark">
      <span class="brand-dot"></span>
      <span class="brand-name">Dova Lenthe</span>
    </div>
  </main>
</body>
</html>
```